UK Supplement Company Needs a Label for Diet Protein Powder

We need a new, modern and fresh design for our Diet Protein Powder. Our protein powder is packaged in black plastic tubs (photo attached) and needs an attractive label. We would like to see designs that grab attention and look professional. We're very open to ideas. The label should be 88mm x 365mm. We also prefer PSD format where possible. These alterations could be made once your design is chosen. Have attached photo of our shake ingredients/benefits.
Updates

Need extra days to review

Target Market(s)

Slimmers

Industry/Entity Type

Health And Wellness

Font styles to use
Serif
Sans Serif

Colors

Designer to choose colors to be used in the design.

Requirements
Must have
• Clean, Modern and Professional Look. Eye catching. The flavour, we offer 6 flavours so this must be something we can edit (Flavours are Banana, Chocolate, Chocolate Mint, Strawberry, Toffee and Vanilla).
Nice to have
• Our logo, this can be BRISK Nutrition or just BRISK. Our logo files are attached.
Should not have
• We do not want to see people (faces or bodies) on the design.

```html
<!DOCTYPE html>
<html lang="en">
<head>
<meta charset="utf-8">
<title>BRISK Nutrition – Diet Protein Powder Label</title>
<link rel="stylesheet" href="https://fonts.googleapis.com/css2?family=Questrial&family=Montserrat:wght@700&family=Roboto+Condensed:wght@700&display=swap">
<style>
  :root {
    --page: #f2f3f4;
    --label-dark: #161718;
    --label-mid: #2a2c2e;
    --blue: #1fa9e8;
    --blue-light: #4fd0fb;
    --blue-deep: #1373b8;
    --white: #ffffff;
    --text-dark: #14263a;
    --choc: #4a2a14;
    --choc-ring: #1a0e06;
  }
  * { margin: 0; padding: 0; box-sizing: border-box; }
  html, body { width: 1200px; height: 1200px; overflow: hidden; background: var(--page); }
  .label {
    position: absolute; left: 50px; top: 200px; width: 1100px; height: 800px;
    background:
      linear-gradient(125deg, transparent 0 30%, rgba(255,255,255,0.06) 42%, transparent 60%),
      radial-gradient(ellipse at 50% 55%, var(--label-mid) 0%, var(--label-dark) 75%);
    overflow: hidden;
  }
  .label-art { position: absolute; inset: 0; width: 1100px; height: 800px; }
  .brand {
    position: absolute; top: 62px; left: 0; width: 100%; text-align: center;
    font-family: "Montserrat", sans-serif; font-weight: 700; font-size: 44px;
    color: var(--white); letter-spacing: 1px;
  }
  .brand-dot {
    display: inline-block; width: 14px; height: 14px; border-radius: 50%;
    background: var(--blue-light); margin-left: 8px; vertical-align: 20px;
  }
  .subtitle {
    position: absolute; top: 202px; left: 0; width: 100%; text-align: center;
    font-family: "Questrial", sans-serif; font-size: 40px; color: var(--white);
    letter-spacing: 3px;
  }
  .title-box {
    position: absolute; top: 258px; left: 182px; width: 736px; height: 212px;
    border: 4px solid var(--blue); outline: 2px solid rgba(255,255,255,0.35); outline-offset: -10px;
    font-family: "Questrial", sans-serif; color: var(--white); text-align: center;
  }
  .title-line { display: block; line-height: 1; }
  .title-line--top { font-size: 104px; margin-top: 8px; letter-spacing: 2px; }
  .title-line--bottom { font-size: 96px; letter-spacing: 50px; margin-left: 50px; margin-top: 2px; }
  .claim {
    position: absolute; top: 490px; left: 175px; width: 750px; height: 60px; border-radius: 30px;
    background: linear-gradient(180deg, var(--blue-light), var(--blue));
    font-family: "Questrial", sans-serif; font-size: 44px; color: var(--text-dark);
    text-align: center; line-height: 62px; letter-spacing: 1px;
  }
  .flavour {
    position: absolute; top: 622px; left: 0; width: 100%; text-align: center;
    font-family: "Roboto Condensed", sans-serif; font-weight: 700; font-size: 44px;
    color: var(--white); letter-spacing: 1px;
  }
  .flavour-swatch {
    display: inline-block; width: 46px; height: 46px; border-radius: 50%;
    background: var(--choc); border: 5px solid var(--choc-ring);
    vertical-align: -8px; margin-right: 14px;
  }
  .net-weight {
    position: absolute; top: 720px; right: 110px; width: 82px; height: 62px;
    border: 2px solid #c9ced3; border-radius: 4px; text-align: center;
    font-family: "Montserrat", sans-serif; font-weight: 700;
  }
  .net-weight-value { display: block; font-size: 28px; color: var(--blue); line-height: 36px; }
  .net-weight-unit { display: block; font-size: 10px; color: var(--white); letter-spacing: 1px; }
</style>
</head>
<body>
  <main class="label">
    <svg class="label-art" viewBox="0 0 1100 800" aria-hidden="true">
      <defs>
        <linearGradient id="band" x1="0" y1="0" x2="1" y2="0">
          <stop offset="0" stop-color="#1a8fd0"/>
          <stop offset="0.5" stop-color="#35c6f7"/>
          <stop offset="1" stop-color="#1a8fd0"/>
        </linearGradient>
        <linearGradient id="swoosh" x1="0" y1="0" x2="1" y2="0">
          <stop offset="0" stop-color="#2bb7f0"/>
          <stop offset="1" stop-color="#1373b8"/>
        </linearGradient>
      </defs>
      <rect class="top-band" x="0" y="0" width="1100" height="22" fill="url(#band)"/>
      <rect class="top-band-shade" x="0" y="22" width="1100" height="10" fill="#10608f"/>
      <path class="bottom-swoosh" d="M0 700 C 220 740, 470 790, 660 800 L 0 800 Z" fill="url(#swoosh)"/>
      <path class="bottom-swoosh-highlight" d="M0 690 C 200 722, 430 770, 660 800 C 430 780, 200 742, 0 712 Z" fill="#6fdcff" opacity="0.8"/>
    </svg>

    <div class="brand">BRISK Nutrition<span class="brand-dot"></span></div>
    <div class="subtitle">DIET PROTEIN POWDER</div>
    <h1 class="title-box">
      <span class="title-line title-line--top">PROTEIN</span>
      <span class="title-line title-line--bottom">SHAKE</span>
    </h1>
    <div class="claim">LOW CALORIE</div>
    <div class="flavour"><span class="flavour-swatch"></span>CHOCOLATE</div>
    <div class="net-weight">
      <span class="net-weight-value">500</span>
      <span class="net-weight-unit">GRAMMS</span>
    </div>
  </main>
</body>
</html>
```